web Design for Architecture and Interior Design Firm

This is a complete redesign of an architecture and interior design firm.( http://www.kelbrixa.com )
We have established a new look-n-feel for them and need to apply it to the new site/new architecture. Wireframes attached with logo and PDF of new brochure.
This will require a quck turn-around. The client is expecting a very modern design with web 2.0 in mind.
Again very quick turn-around! If you cannot commit to a Friday deliverable, do not bid! Must be completed by no later than Friday!

```html
<!DOCTYPE html>
<html lang="en">
<head>
<meta charset="utf-8">
<title>Varlow Brenner Design Studios</title>
<link href="https://fonts.googleapis.com/css2?family=PT+Sans:wght@400;700&family=Arimo:wght@400;700&display=swap" rel="stylesheet">
<style>
:root{
  --brown:#6b5d4b;
  --brown-dark:#5c4f3f;
  --red:#c0163a;
  --red-dark:#9c0f2c;
  --ink:#2b2b2b;
  --text:#3a3a3a;
  --page:#cdcdcd;
  --band:#e6e6e6;
  --line:#b9b9b9;
  --white:#ffffff;
  --contact:#5b5b5b;
  --mark:#8a8a8a;
}
*{margin:0;padding:0;box-sizing:border-box}
html,body{width:1200px;height:829px;overflow:hidden;background:var(--page)}
.stage{position:absolute;left:0;top:0;width:1280px;height:884px;transform:scale(.9375);transform-origin:0 0;
  font-family:"Arimo",Arial,sans-serif;color:var(--text);background:var(--page)}
.abs{position:absolute}
.header{left:0;top:0;width:1280px;height:140px;background:linear-gradient(#e4e4e4,#ffffff 70%)}
.brand{left:160px;top:48px;display:flex;align-items:center;gap:12px;
  font-family:"PT Sans",sans-serif;font-weight:400;font-size:38px;line-height:42px;color:var(--ink)}
.brand .mark{width:12px;height:12px;background:var(--mark)}
.contact{left:847px;top:0;width:273px;height:80px;background:var(--contact);border-radius:0 0 4px 4px;box-shadow:0 3px 3px rgba(0,0,0,.25);
  color:#fff;font-family:"PT Sans",sans-serif;font-size:15px}
.contact .row{position:absolute;left:17px;display:flex;align-items:center;gap:10px}
.contact b{font-size:16px}
.nav{left:590px;top:102px;display:flex;font-family:"PT Sans",sans-serif;font-size:15px;color:var(--ink)}
.nav a{display:block;padding:8px 0 0;margin-right:34px;color:inherit;text-decoration:none;border-top:3px solid transparent}
.nav a.active{border-top-color:var(--red)}
.nav .caret{font-size:9px;margin-left:4px}
.main{left:160px;top:140px;width:960px;height:631px;background:var(--white)}
.hero-band{left:160px;top:140px;width:960px;height:33px;background:var(--band)}
.hero-photo{left:455px;top:173px;width:665px;height:234px;background:linear-gradient(100deg,#5b5550 0%,#8a7c6b 35%,#b98a4d 65%,#d7a760 100%)}
.hero-panel{left:160px;top:140px}
.hero-title{left:180px;top:184px;color:#fff;font-family:"PT Sans",sans-serif;font-size:23px}
.hero-list{left:193px;top:234px;list-style:none;color:#fff;font-size:14.5px}
.hero-list li{height:24px;display:flex;align-items:center;gap:10px}
.hero-list li::before{content:"";width:8px;height:8px;border:1.5px solid #fff;border-radius:50%}
.btn{display:flex;align-items:center;justify-content:center;color:#fff;font-family:"PT Sans",sans-serif;font-size:15px;border-radius:15px;
  background:linear-gradient(#e0385a,var(--red) 50%,var(--red-dark))}
.slider-bar{left:455px;top:407px;width:365px;height:33px;background:var(--band);font-family:"PT Sans",sans-serif;font-size:15px;color:#111;padding:7px 0 0 12px}
.slider-bar span{color:var(--red)}
.services{left:820px;top:407px;width:300px;height:277px;background:linear-gradient(#f0f0f0,#cfcfcf)}
.services-head{left:820px;top:407px;width:305px;height:48px}
.services-head h2{position:absolute;left:20px;top:9px;color:#fff;font-family:"PT Sans",sans-serif;font-weight:400;font-size:19px}
.services-intro{left:840px;top:463px;width:240px;font-size:12.5px;line-height:18.5px;color:#333}
.arrow-list{list-style:none;font-size:12.5px;color:#333}
.arrow-list li{height:24px;display:flex;align-items:center;gap:12px}
.arrow-list li svg{flex:none}
.services-list{left:840px;top:531px}
.services-foot{left:820px;top:678px;width:300px;height:6px;background:var(--brown)}
.tabs{left:160px;top:440px}
.tab-links{left:204px;top:455px;display:flex;gap:31px;font-family:"PT Sans",sans-serif;font-size:14.5px;color:var(--ink)}
.tab-links .on{color:var(--red)}
.about-title{left:180px;top:495px;font-family:"PT Sans",sans-serif;font-weight:400;font-size:19px;color:var(--ink)}
.about-title span{color:var(--red)}
.about-copy{left:180px;top:530px;width:620px;font-size:12.5px;line-height:18.5px;color:#333}
.about-since{left:180px;top:596px;font-size:12.5px;color:#333}
.about-col1{left:193px;top:616px}
.about-col2{left:556px;top:616px}
.footer{left:180px;top:736px;width:920px;height:130px;background:var(--band);border:1px solid var(--line);border-top:2px solid #a8a8a8}
.footer-top{left:180px;top:738px;width:920px;height:33px;background:#f6f6f6;border-bottom:1px solid var(--line)}
.footer-col{font-size:12.5px;color:#222}
.footer-col h3{font-size:13px;font-weight:700;height:33px;padding-top:7px;color:#111;font-family:"Arimo",Arial,sans-serif}
.footer-col ul{padding-top:9px}
.footer-col li{list-style:none;height:18px}
.footer-col .on{color:var(--red)}
.copyright{left:855px;top:744px;font-size:11px;color:#333}
.copyright span{color:var(--brown)}
.footer-brand{left:878px;top:802px;font-size:24px;line-height:28px;gap:8px}
.footer-brand .mark{width:8px;height:8px}
</style>
</head>
<body>
<div class="stage">
  <div class="abs header"></div>

  <div class="abs brand"><span>Varlow Brenner</span><span class="mark"></span></div>

  <div class="abs contact">
    <div class="row" style="top:11px">
      <svg width="24" height="18" viewBox="0 0 24 18"><rect x="0.5" y="0.5" width="23" height="17" fill="none" stroke="#fff"/><path d="M7 4c-1 1-1 3 1 6s4 4 6 4l1-2-2-1-1 1c-1 0-3-2-3-3l1-1-1-2z" fill="#fff"/></svg>
      <span style="margin-left:14px">Call Us: <b>555.218.0147 x121</b></span>
    </div>
    <div class="row" style="top:43px">
      <svg width="24" height="18" viewBox="0 0 24 18"><rect x="0.5" y="0.5" width="23" height="17" fill="none" stroke="#fff"/><path d="M1 1l11 9 11-9M1 17l8-8M23 17l-8-8" fill="none" stroke="#fff"/></svg>
      <span>email: <b>admin@kelbrixa.com</b></span>
    </div>
  </div>

  <nav class="abs nav">
    <a href="#" style="margin-right:44px">Home</a>
    <a href="#" class="active">About Us<span class="caret">▼</span></a>
    <a href="#">Services<span class="caret">▼</span></a>
    <a href="#">Portfolio<span class="caret">▼</span></a>
    <a href="#">News<span class="caret">▼</span></a>
    <a href="#">Contact</a>
  </nav>

  <div class="abs main"></div>

  <div class="abs hero-band"></div>
  <div class="abs hero-photo" role="img" aria-label="Photo of a studio reception area with wood-panelled walls, a company sign and lounge chairs"></div>
  <svg class="abs hero-panel" width="360" height="300" viewBox="0 0 360 300"><polygon points="0,0 350,0 295,300 0,300" fill="var(--brown)"/></svg>
  <div class="abs hero-title">Halden Pryce, Ridgefield, VA</div>
  <ul class="abs hero-list">
    <li>10,000 SF</li>
    <li>Secure information area</li>
    <li>Editing suites and studios</li>
    <li>Demonstration lab</li>
    <li>Open ceilings</li>
  </ul>
  <div class="abs btn" style="left:306px;top:392px;width:119px;height:30px">Read More</div>

  <div class="abs slider-bar">1/ 10 | <span>Slide 1</span>
    <svg style="position:absolute;left:328px;top:8px" width="28" height="18" viewBox="0 0 28 18"><path d="M0 0h7l9 9-9 9H0l9-9z" fill="var(--red)"/><path d="M11 0h7l9 9-9 9h-7l9-9z" fill="var(--brown)"/></svg>
  </div>

  <div class="abs services"></div>
  <svg class="abs services-head" width="305" height="48" viewBox="0 0 305 48"><path d="M0 0h300a5 5 0 0 1 5 5v39a4 4 0 0 1-4 4h-1V40H0z" fill="var(--brown)"/><rect x="300" y="0" width="5" height="48" fill="var(--brown-dark)"/></svg>
  <div class="abs services-head"><h2>Services</h2></div>
  <p class="abs services-intro">We are committed to providing services that result in environments that meet our clients' needs and desired image.</p>
  <ul class="abs arrow-list services-list">
    <li><svg width="7" height="9" viewBox="0 0 7 9"><path d="M0 0h3l4 4.5L3 9H0l4-4.5z" fill="var(--red)"/></svg>Architectural</li>
    <li><svg width="7" height="9" viewBox="0 0 7 9"><path d="M0 0h3l4 4.5L3 9H0l4-4.5z" fill="var(--red)"/></svg>Engineering</li>
    <li><svg width="7" height="9" viewBox="0 0 7 9"><path d="M0 0h3l4 4.5L3 9H0l4-4.5z" fill="var(--red)"/></svg>Interior Design</li>
    <li><svg width="7" height="9" viewBox="0 0 7 9"><path d="M0 0h3l4 4.5L3 9H0l4-4.5z" fill="var(--red)"/></svg>Facility Management</li>
  </ul>
  <div class="abs btn" style="left:981px;top:634px;width:99px;height:30px;border-radius:6px">Read More</div>
  <div class="abs services-foot"></div>

  <svg class="abs tabs" width="660" height="40" viewBox="0 0 660 40">
    <rect x="20" y="10" width="620" height="30" fill="var(--band)"/>
    <polygon points="0,0 20,10 20,40" fill="#a9a9a9"/>
    <polygon points="660,0 640,10 640,40" fill="#a9a9a9"/>
  </svg>
  <div class="abs tab-links"><span class="on">About Us</span><span>RDA Alliance</span><span>History</span><span>Firm Principals</span><span>Our Mission</span></div>

  <h1 class="abs about-title">About <span>The Varlow Brenner Design Studios</span></h1>
  <p class="abs about-copy">Lorem Ipsum is simply dummy text of the printing and typesetting industry. Lorem Ipsum has been the industry's standard dummy text ever since the 1500s, when an unknown printer took a galley of type and scrambled it to make a type specimen book.</p>
  <p class="abs about-since">We've been providing answers since 1985.</p>
  <ul class="abs arrow-list about-col1">
    <li><svg width="7" height="9" viewBox="0 0 7 9"><path d="M0 0h3l4 4.5L3 9H0l4-4.5z" fill="var(--red)"/></svg>Founded 1985</li>
    <li><svg width="7" height="9" viewBox="0 0 7 9"><path d="M0 0h3l4 4.5L3 9H0l4-4.5z" fill="var(--red)"/></svg>Working with facility managers, owners and tenants</li>
    <li><svg width="7" height="9" viewBox="0 0 7 9"><path d="M0 0h3l4 4.5L3 9H0l4-4.5z" fill="var(--red)"/></svg>Designs resulting in the best value for your build-out dollar</li>
    <li><svg width="7" height="9" viewBox="0 0 7 9"><path d="M0 0h3l4 4.5L3 9H0l4-4.5z" fill="var(--red)"/></svg>Integration of architectural and engineering design</li>
  </ul>
  <ul class="abs arrow-list about-col2">
    <li><svg width="7" height="9" viewBox="0 0 7 9"><path d="M0 0h3l4 4.5L3 9H0l4-4.5z" fill="var(--red)"/></svg>Creating your desired image</li>
    <li><svg width="7" height="9" viewBox="0 0 7 9"><path d="M0 0h3l4 4.5L3 9H0l4-4.5z" fill="var(--red)"/></svg>Building long lasting trusting relationships</li>
    <li><svg width="7" height="9" viewBox="0 0 7 9"><path d="M0 0h3l4 4.5L3 9H0l4-4.5z" fill="var(--red)"/></svg>Projects completed on schedule</li>
    <li><svg width="7" height="9" viewBox="0 0 7 9"><path d="M0 0h3l4 4.5L3 9H0l4-4.5z" fill="var(--red)"/></svg>LEED Certified designers</li>
  </ul>

  <footer>
    <div class="abs footer"></div>
    <div class="abs footer-top"></div>
    <div class="abs footer-col" style="left:199px;top:738px"><h3>Home</h3></div>
    <div class="abs footer-col" style="left:282px;top:738px"><h3>About Us</h3><ul><li>RDA Alliance</li><li>History</li><li>Firm Principals</li><li>Our Mission</li></ul></div>
    <div class="abs footer-col" style="left:423px;top:738px"><h3>Services</h3><ul><li class="on">Architectural</li><li>Engineering</li><li>Interior Design</li><li>Facility Management</li></ul></div>
    <div class="abs footer-col" style="left:567px;top:738px"><h3>Portfolio</h3><ul><li>Clients</li><li>Testimonial</li></ul></div>
    <div class="abs footer-col" style="left:705px;top:738px"><h3>News</h3><ul><li>Newsletter</li><li>Awards</li><li>Firm Events</li><li>20th Anniversary</li></ul></div>
    <div class="abs copyright">Copyright 2011. <span>Varlow Brenner Design Studios</span>.</div>
    <div class="abs brand footer-brand"><span>Varlow Brenner</span><span class="mark"></span></div>
  </footer>
</div>
</body>
</html>
```